Solar Billboard Design

We require a billboard 24ftx10ft in size for our solar company.
Artwork Requirement’s:
• Sent on PDF file
• At least 300 dpi
• Scaled to 25% of banner size (24ft x 10ft)
• Please allow at least 40mm space from the artwork edge to allow for any hems and eyelets. This will ensure any important text/images are not cropped/overlapped.
The billboard must have on it:
Solar & Battery Packages
From £8750
In Stock Now!
brightfieldpower.co.uk (must stand out)
________________________
I have attached our logo and some images. I'm not sure if they are good enough quality so you may need to use a stock image.
Kind regards,
Marcus
Target Market(s)
Men & Women aged 35-70, homeowners
Industry/Entity Type
Solar / Construction
Look and feel
Each slider illustrates characteristics of the customer's brand and the style your logo design should communicate.

```html
<!DOCTYPE html>
<html lang="en">
<head>
<meta charset="utf-8">
<title>Brightfield Energy Group – Solar &amp; Battery Billboard</title>
<link href="https://fonts.googleapis.com/css2?family=Poppins:wght@400;500;600;700;800&family=Oswald:wght@500&display=swap" rel="stylesheet">
<style>
  :root {
    --page: #cbcbcb;
    --white: #ffffff;
    --ink: #3f3d3f;
    --badge: #474447;
    --green: #2ecc66;
    --halo: #d9d7d8;
    --sky: #4f7cbf;
    --roof: #d9733f;
    --wall: #e8ddd0;
  }
  html, body {
    margin: 0;
    width: 1200px;
    height: 1200px;
    overflow: hidden;
    background: var(--page);
  }
  .billboard {
    position: absolute;
    left: 80px;
    top: 384px;
    width: 1042px;
    height: 433px;
    display: block;
  }
  .heading { font-family: "Poppins", sans-serif; }
  .heading--dark { fill: var(--ink); font-weight: 800; }
  .heading--green { fill: var(--green); font-weight: 800; }
  .subheading { fill: var(--ink); font-family: "Poppins", sans-serif; font-weight: 500; }
  .brand-name { fill: var(--ink); font-family: "Poppins", sans-serif; font-weight: 400; font-size: 28px; }
  .stock-text { font-family: "Poppins", sans-serif; font-weight: 700; font-size: 50px; }
  .url-text { font-family: "Poppins", sans-serif; font-weight: 600; font-size: 54px; }
  .price-from { fill: var(--green); font-family: "Poppins", sans-serif; font-weight: 600; font-size: 42px; }
  .price-value { fill: var(--white); font-family: "Oswald", sans-serif; font-weight: 500; }
</style>
</head>
<body>
<svg class="billboard" viewBox="128 618 1678 698" xmlns="http://www.w3.org/2000/svg">
  <defs>
    <linearGradient id="houseTones" x1="0" y1="0" x2="0" y2="1">
      <stop offset="0" stop-color="var(--sky)"/>
      <stop offset="0.17" stop-color="var(--sky)"/>
      <stop offset="0.24" stop-color="var(--roof)"/>
      <stop offset="0.68" stop-color="var(--roof)"/>
      <stop offset="0.72" stop-color="var(--wall)"/>
      <stop offset="1" stop-color="var(--wall)"/>
    </linearGradient>
  </defs>

  <rect class="canvas" x="128" y="618" width="1678" height="698" fill="var(--white)"/>

  <path class="accent-band" d="M1030 618 L910 676 Q835 715 840 790 Q845 860 900 940 L1010 1190 H128 V1316 H1806 V618 Z" fill="var(--green)"/>

  <path class="house-photo" role="img" aria-label="Photo of a house with an orange tiled roof covered in solar panels under a blue sky"
        d="M1140 618 H1806 V1316 H1135 L905 820 Q890 760 950 718 Z" fill="url(#houseTones)"/>

  <path class="stock-bar" d="M128 1103 H725 Q765 1103 785 1190 H128 Z" fill="var(--badge)"/>

  <circle class="price-halo" cx="935" cy="950" r="147" fill="var(--halo)" opacity="0.75"/>
  <circle class="price-badge" cx="932" cy="950" r="122" fill="var(--badge)"/>
  <text class="price-from" x="935" y="922" text-anchor="middle">FROM</text>
  <text class="price-value" x="932" y="1003" text-anchor="middle"><tspan font-size="42" dy="-30">£</tspan><tspan font-size="84" dy="30">8750</tspan></text>

  <g class="brand">
    <circle class="brand-mark" cx="262" cy="748" r="36" fill="var(--green)"/>
    <text class="brand-name" x="312" y="722" letter-spacing="4">BRIGHTFIELD</text>
    <text class="brand-name" x="312" y="755" letter-spacing="4">ENERGY</text>
    <text class="brand-name" x="312" y="787" letter-spacing="4">GROUP</text>
  </g>

  <text class="heading heading--dark" x="214" y="912" font-size="110" textLength="508" lengthAdjust="spacingAndGlyphs">SOLAR &amp;</text>
  <text class="heading heading--green" x="214" y="1012" font-size="112" textLength="538" lengthAdjust="spacingAndGlyphs">BATTERY</text>
  <text class="subheading" x="218" y="1065" font-size="54" textLength="534" lengthAdjust="spacing">PACKAGES</text>

  <text class="stock-text" x="216" y="1167" fill="var(--white)">IN STOCK <tspan fill="var(--green)">NOW!</tspan></text>

  <text class="url-text" x="215" y="1265" textLength="800" lengthAdjust="spacingAndGlyphs" fill="var(--white)">www.Brightfield<tspan fill="var(--ink)">Power</tspan>.co.uk</text>
</svg>
</body>
</html>
```